Need a graphic designer for creating some infographic technology backgrounds

I need a graphic designer who can do professionally infographic technology and finance backgrounds of around 200 as per my requirements.

Please check my samples which I wanted to create like these samples.

```html
<!DOCTYPE html>
<html lang="en">
<head>
<meta charset="utf-8">
<title>Technology Infographic</title>
<link rel="stylesheet" href="https://fonts.googleapis.com/css2?family=Raleway:wght@500;600&family=Roboto+Condensed:wght@600&family=Open+Sans:wght@400;700&display=swap">
<style>
  :root {
    --bg-deep: #071a36;
    --bg-mid: #0d2f5c;
    --bg-light: #134477;
    --cyan: #4fd1f5;
    --sky: #6ebff0;
    --blue: #3a7be6;
    --violet: #9a6cf2;
    --text: #ffffff;
    --text-soft: #e3ecf7;
    --circuit: #2f6aa6;
  }
  * { margin: 0; padding: 0; box-sizing: border-box; }
  html, body { width: 1200px; height: 799px; overflow: hidden; background: var(--bg-deep); }
  .canvas {
    position: relative; width: 1200px; height: 799px; overflow: hidden;
    background:
      radial-gradient(circle at 20% 25%, var(--bg-light) 0%, transparent 45%),
      linear-gradient(120deg, var(--bg-mid) 0%, var(--bg-deep) 75%);
    font-family: "Open Sans", sans-serif; color: var(--text);
  }
  .hex-field {
    position: absolute; left: 0; top: 0; width: 520px; height: 150px;
    background: radial-gradient(ellipse at 40% 0%, rgba(70,140,210,0.28) 0%, rgba(70,140,210,0.08) 55%, transparent 80%);
  }
  .circuit-lines { position: absolute; left: 0; top: 0; }
  .title {
    position: absolute; left: 62px; top: 72px;
    font-family: "Raleway", sans-serif; font-weight: 600; font-size: 80px; letter-spacing: -1px;
    background: linear-gradient(90deg, var(--cyan), var(--blue) 70%, var(--violet));
    -webkit-background-clip: text; background-clip: text; color: transparent;
  }
  .subtitle {
    position: absolute; left: 68px; top: 178px;
    font-family: "Raleway", sans-serif; font-weight: 500; font-size: 29px; letter-spacing: 10px;
    color: var(--text-soft);
  }
  .intro { position: absolute; left: 68px; top: 236px; font-size: 14px; line-height: 26px; color: var(--text-soft); }
  .step { position: absolute; left: 68px; width: 420px; }
  .step-number {
    position: absolute; left: 0; top: 0;
    font-family: "Roboto Condensed", sans-serif; font-weight: 600; font-size: 76px; line-height: 76px;
    color: var(--sky);
  }
  .step-heading {
    position: absolute; left: 94px; top: 0; white-space: nowrap;
    font-weight: 700; font-size: 19px; letter-spacing: 6px;
  }
  .step-text {
    position: absolute; left: 94px; top: 32px; width: 300px;
    font-size: 13.5px; line-height: 18px; color: var(--text-soft);
  }
  .step-1 { top: 322px; }
  .step-2 { top: 449px; }
  .step-3 { top: 575px; }
  .icon { position: absolute; color: var(--sky); }
  .icon-chip { left: 454px; top: 356px; }
  .icon-team { left: 458px; top: 462px; }
  .icon-binary {
    left: 461px; top: 584px;
    font-family: "Roboto Condensed", sans-serif; font-weight: 600; font-size: 31px; line-height: 33px;
    letter-spacing: 1px;
  }
  .tech-dial {
    position: absolute; left: 570px; top: 126px; width: 580px; height: 580px; border-radius: 50%;
    background:
      radial-gradient(circle at 30% 18%, rgba(255,255,255,0.55) 0%, transparent 18%),
      radial-gradient(circle at 50% 50%, #4f7fa8 0%, #35679a 22%, #1d4f8a 36%, #2a63b0 52%, #4a6ad8 64%, #0f3566 74%, #0c2b55 100%);
    box-shadow: 60px 60px 120px rgba(150,100,240,0.18);
  }
</style>
</head>
<body>
<main class="canvas">
  <div class="hex-field" role="img" aria-label="Faint honeycomb pattern"></div>

  <svg class="circuit-lines" width="600" height="799" viewBox="0 0 600 799" fill="none" stroke="var(--circuit)" stroke-width="1.2" opacity="0.55">
    <path d="M0 300h40l22-22h160l20 20h310"/>
    <path d="M0 330h70l20 20h70"/>
    <path d="M0 410h30l20-20h60"/>
    <path d="M0 440h90l24 24h460"/>
    <path d="M0 520h60l24 24h150"/>
    <path d="M300 420h120l20-20h140"/>
    <path d="M400 540h180"/>
    <g fill="var(--circuit)" stroke="none">
      <circle cx="40" cy="300" r="3"/><circle cx="160" cy="350" r="3"/>
      <circle cx="110" cy="390" r="3"/><circle cx="234" cy="544" r="3"/>
      <circle cx="300" cy="420" r="3"/><circle cx="400" cy="540" r="3"/>
    </g>
  </svg>

  <h1 class="title">Technology</h1>
  <p class="subtitle">INFOGRAPHIC</p>
  <p class="intro">Lorem ipsum dolor sit amet, consectetuer adipiscing elit,<br>sed diam nonummy nibh.</p>

  <section class="step step-1">
    <span class="step-number">01</span>
    <h2 class="step-heading">LOREM IPSUM</h2>
    <p class="step-text">Lorem ipsum dolor sit amet, consectetuer adipiscing elit, sed diam nonummy nibh euismod tincidunt ut laoreet</p>
  </section>
  <section class="step step-2">
    <span class="step-number">02</span>
    <h2 class="step-heading">LOREM IPSUM</h2>
    <p class="step-text">Lorem ipsum dolor sit amet, consectetuer adipiscing elit, sed diam nonummy nibh euismod tincidunt ut laoreet</p>
  </section>
  <section class="step step-3">
    <span class="step-number">03</span>
    <h2 class="step-heading">LOREM IPSUM</h2>
    <p class="step-text">Lorem ipsum dolor sit amet, consectetuer adipiscing elit, sed diam nonummy nibh euismod tincidunt ut laoreet</p>
  </section>

  <svg class="icon icon-chip" width="52" height="52" viewBox="0 0 52 52" fill="none" stroke="currentColor" stroke-width="2.5">
    <rect x="12" y="12" width="28" height="28" rx="3"/>
    <rect x="18" y="18" width="16" height="16" fill="currentColor"/>
    <path d="M19 4v8M26 4v8M33 4v8M19 40v8M26 40v8M33 40v8M4 19h8M4 26h8M4 33h8M40 19h8M40 26h8M40 33h8"/>
  </svg>

  <svg class="icon icon-team" width="60" height="60" viewBox="0 0 60 60" fill="none" stroke="currentColor" stroke-width="2">
    <polygon points="15,2 26,8 26,20 15,26 4,20 4,8"/>
    <polygon points="43,16 54,22 54,34 43,40 32,34 32,22"/>
    <polygon points="15,32 26,38 26,50 15,56 4,50 4,38"/>
    <g fill="currentColor" stroke="none">
      <circle cx="15" cy="11" r="3"/><path d="M9 20a6 5 0 0 1 12 0z"/>
      <circle cx="43" cy="25" r="3"/><path d="M37 34a6 5 0 0 1 12 0z"/>
      <circle cx="15" cy="41" r="3"/><path d="M9 50a6 5 0 0 1 12 0z"/>
    </g>
  </svg>

  <div class="icon icon-binary">010<br>101</div>

  <div class="tech-dial" role="img" aria-label="Glowing circular tech dial with neon rings around a world globe"></div>
</main>
</body>
</html>
```